Heron valley RV Resort business card

I need a design card for the logo I just had made on here. I will provide it and please make some cool designs, thank you.

I would like the card to have
- phone number (865-318-2967)
- email ( heronvalleyrv@pinemail.com)
- address to the park ( 5186 Quarry Gate Loop rd, Maryville, TN) ZIP: 37429
on the back for double sided id like some lines for writing on. thanks

please follow the logo we provided in the files, I can provide the photoshop file if you need it.

please note this is in the Smokey mountains of Tennessee

Target Market(s)

cabin/rv rentals

Industry/Entity Type

rv/campground/cabin rentals

Contact Information for Business Card

address/email/phone number I added details in brief

Requirements
Must have
• on the back add a bear or something cool

```html
<!DOCTYPE html>
<html lang="en">
<head>
<meta charset="utf-8">
<title>Heron valley RV Resort – Business Card</title>
<link rel="stylesheet" href="https://fonts.googleapis.com/css2?family=Arimo:wght@400;700&display=swap">
<style>
  :root {
    --page-bg: #e6e6e6;
    --card-bg: #ffffff;
    --sky-top: #ee6a3a;
    --sky-mid: #f8b52a;
    --sky-low: #f6e43a;
    --ridge-blue: #5f86b8;
    --forest-dark: #15190f;
    --ink: #4a4a4a;
    --ink-soft: #666666;
    --accent: #a8381f;
    --rule: #8a8a8a;
    --dash: #9a9a9a;
    --ghost: #ececec;
  }
  * { margin: 0; padding: 0; box-sizing: border-box; }
  html, body { width: 1200px; height: 900px; overflow: hidden; }
  body {
    background: var(--page-bg);
    font-family: "Arimo", Arial, sans-serif;
    color: var(--ink);
    position: relative;
  }
  .card {
    position: absolute;
    left: 250px;
    width: 700px;
    height: 400px;
    background: var(--card-bg);
    box-shadow: 0 6px 18px rgba(0,0,0,0.18);
    overflow: hidden;
  }
  .card--back { top: 35px; }
  .card--front { top: 465px; }

  /* Back */
  .scenery-band {
    position: absolute; left: 0; top: 0; width: 100%; height: 185px;
    background: linear-gradient(180deg, var(--sky-top) 0%, var(--sky-mid) 38%, var(--sky-low) 58%, var(--ridge-blue) 78%, var(--forest-dark) 100%);
  }
  .brand-mark {
    position: absolute; display: flex; align-items: center; gap: 8px;
    font-weight: 700; font-size: 17px; color: var(--forest-dark); letter-spacing: 0.5px;
  }
  .card--back .brand-mark { right: 40px; top: 30px; }
  .brand-dot {
    width: 14px; height: 14px; border-radius: 50%; background: var(--forest-dark); flex: none;
  }
  .writing-lines { position: absolute; left: 60px; right: 40px; top: 225px; }
  .writing-line { border-top: 1.5px dashed var(--dash); height: 48px; }

  /* Front */
  .faint-decoration {
    position: absolute; left: 20px; top: 90px; width: 440px; height: 330px;
    border-radius: 50% 50% 0 0;
    background: radial-gradient(ellipse at 50% 45%, var(--ghost) 0%, rgba(236,236,236,0.4) 60%, rgba(255,255,255,0) 80%);
  }
  .card--front .brand-mark { right: 40px; top: 60px; font-size: 19px; }
  .address-rule {
    position: absolute; left: 40px; right: 40px; top: 150px; border-top: 1.5px solid var(--rule);
  }
  .address {
    position: absolute; right: 40px; top: 165px; text-align: right;
    font-size: 19px; line-height: 1.2; color: var(--ink-soft);
  }
  .person { position: absolute; left: 40px; top: 250px; }
  .person-name { font-weight: 700; font-size: 26px; color: var(--accent); letter-spacing: 0.5px; }
  .person-role { font-size: 20px; color: var(--ink-soft); margin-top: 2px; }
  .contact-rule { position: absolute; left: 40px; width: 470px; top: 315px; border-top: 1.5px solid var(--rule); }
  .contacts { position: absolute; left: 40px; top: 327px; list-style: none; }
  .contact-item { display: flex; align-items: center; gap: 12px; font-size: 19px; color: var(--ink-soft); height: 27px; }
  .contact-icon { width: 16px; height: 16px; flex: none; }
</style>
</head>
<body>

  <section class="card card--back" aria-label="Business card back">
    <div class="scenery-band" role="img" aria-label="Illustration of a sunset over blue Smoky Mountain ridges with dark pine tree silhouettes"></div>
    <div class="brand-mark"><span class="brand-dot"></span>Heron valley RV Resort</div>
    <div class="writing-lines">
      <div class="writing-line"></div>
      <div class="writing-line"></div>
      <div class="writing-line"></div>
    </div>
  </section>

  <section class="card card--front" aria-label="Business card front">
    <div class="faint-decoration" role="img" aria-label="Faint decorative emblem with pine trees in light grey"></div>
    <div class="brand-mark"><span class="brand-dot"></span>Heron valley RV Resort</div>
    <div class="address-rule"></div>
    <p class="address">5186 Quarry Gate Loop rd<br>Maryville, TN&nbsp; 37429</p>
    <div class="person">
      <p class="person-name">MARCUS ELLERY</p>
      <p class="person-role">Manager</p>
    </div>
    <div class="contact-rule"></div>
    <ul class="contacts">
      <li class="contact-item">
        <svg class="contact-icon" viewBox="0 0 16 16" aria-hidden="true">
          <path d="M3 1.5 L6 1.5 L7 5 L5.2 6.3 C6 8.2 7.8 10 9.7 10.8 L11 9 L14.5 10 L14.5 13 C14.5 14 13.6 14.6 12.6 14.5 C6.8 13.8 2.2 9.2 1.5 3.4 C1.4 2.4 2 1.5 3 1.5 Z" fill="var(--accent)"/>
        </svg>
        865-318-2967
      </li>
      <li class="contact-item">
        <svg class="contact-icon" viewBox="0 0 16 16" aria-hidden="true">
          <rect x="1.5" y="3.5" width="13" height="9" rx="1" fill="none" stroke="var(--accent)" stroke-width="1.6"/>
          <path d="M1.8 4 L8 9 L14.2 4" fill="none" stroke="var(--accent)" stroke-width="1.6"/>
        </svg>
        heronvalleyrv@pinemail.com
      </li>
    </ul>
  </section>

</body>
</html>
```